Tarjetas de visita para empresa de aluminio

Empresa con mas de 40 años vendiendo perfiles de aluminio.
Somos fábrica y almacén, queremos renovar la tarjeta de presentación de nuestros comerciales dando una imgen innovadora y tecnógica mezclado con la calidez del respeto al medio ambiente.
Añado el logo de la empresa y actual cara trasera de la tarjeta de visita, el logo es el simbolo WM y la marca TRAVENIC EXTRUSION, la frase 2extrusion y lacado de aluminio" debe cambiarse por "Diseño, extrusión, lacado, anodizado y mecanizado de precisión de aluminio" o en su defecto incluir todos esos servicios que hacemos o una frase mas pegadiza.

We are an aluminium factory, we produce and stock profiles of aluminium.
we want to renew visit card of our sellers, we are looking for something that show innovation, tecnology and environment respect.
Upload our actual logo and back of visit card, logo WM and brand TRAVENIC EXTRUSION must be keept.
Text "Extrusion y lacado de aluminio" must be changed for "Diseño, extrusion, lacado, anodizado y mecanizado de precisión de aluminio" or something like that

```html
<!DOCTYPE html>
<html lang="es">
<head>
<meta charset="utf-8">
<title>Travenic Extrusion – Tarjetas de visita</title>
<link href="https://fonts.googleapis.com/css2?family=Montserrat:wght@400;600;700&display=swap" rel="stylesheet">
<style>
  :root {
    --stage: #2b2b2c;
    --card-black: #1a1a1b;
    --card-graphite: #2e2f31;
    --silver-light: #f2f2f3;
    --silver-mid: #bfc0c2;
    --silver-dark: #8d8e91;
    --chrome-text: #e4e5e7;
    --muted-text: #b9babd;
    --rule: #9a9b9e;
  }
  * { box-sizing: border-box; margin: 0; padding: 0; }
  html, body {
    width: 1200px; height: 1186px; overflow: hidden;
    background: var(--stage);
    font-family: "Montserrat", sans-serif;
  }
  .canvas { position: relative; width: 1200px; height: 1186px; }

  .card {
    position: absolute; left: 170px;
    width: 860px; height: 491px;
    border-radius: 30px; overflow: hidden;
  }

  /* Front */
  .card--front { top: 72px; background: var(--card-black); }
  .front__band {
    position: absolute; left: 0; top: 0; width: 100%; height: 210px;
    background: linear-gradient(100deg, var(--silver-dark) 0%, var(--silver-light) 35%, var(--silver-mid) 60%, var(--silver-light) 85%, var(--silver-mid) 100%);
  }
  .front__brand {
    position: absolute; left: 0; right: 0; top: 110px;
    display: flex; flex-direction: column; align-items: center;
  }
  .brand-mark {
    display: flex; align-items: center; justify-content: center;
    border-radius: 50%;
    background: var(--card-black);
    border: 3px solid var(--chrome-text);
    color: var(--chrome-text); font-weight: 600;
  }
  .front__brand .brand-mark { width: 190px; height: 190px; font-size: 66px; letter-spacing: 4px; }
  .brand-name {
    color: var(--chrome-text); font-weight: 600; text-transform: uppercase; white-space: nowrap;
  }
  .front__brand .brand-name { margin-top: 26px; font-size: 50px; letter-spacing: 6px; }
  .tagline {
    color: var(--chrome-text); font-weight: 400; text-transform: uppercase; text-align: center;
  }
  .front__brand .tagline { margin-top: 14px; font-size: 20px; letter-spacing: 3px; line-height: 1.45; }

  /* Back */
  .card--back {
    top: 622px;
    background: linear-gradient(135deg, var(--card-graphite) 0%, #242527 55%, var(--card-black) 100%);
  }
  .back__brand {
    position: absolute; left: 40px; top: 0; width: 390px; height: 100%;
    display: flex; flex-direction: column; align-items: center; justify-content: center;
  }
  .back__brand .brand-mark { width: 120px; height: 120px; font-size: 40px; letter-spacing: 3px; }
  .back__brand .brand-name { margin-top: 16px; font-size: 28px; letter-spacing: 3px; }
  .back__brand .tagline { margin-top: 8px; font-size: 11.5px; letter-spacing: 1.5px; line-height: 1.5; }

  .back__divider {
    position: absolute; left: 460px; top: 70px; width: 2px; height: 350px;
    background: var(--rule);
  }
  .contact { position: absolute; left: 500px; top: 80px; width: 340px; color: var(--muted-text); }
  .contact__name { color: #fff; font-weight: 700; font-size: 23px; letter-spacing: 0.5px; }
  .contact__role { font-size: 16px; margin-top: 4px; }
  .contact__list { list-style: none; margin-top: 20px; }
  .contact__list li { display: flex; align-items: center; gap: 12px; font-size: 16px; line-height: 1.75; }
  .contact__list svg { width: 16px; height: 16px; fill: var(--muted-text); flex: none; }
  .contact__address { margin-top: 22px; font-size: 15.5px; line-height: 1.45; font-style: normal; }
</style>
</head>
<body>
<main class="canvas">

  <section class="card card--front" aria-label="Cara delantera">
    <div class="front__band"></div>
    <div class="front__brand">
      <div class="brand-mark">WM</div>
      <p class="brand-name">Travenic Extrusion</p>
      <p class="tagline">Diseño · Extrusion · Lacado · Anodizado<br>y mecanizado de precisión de aluminio</p>
    </div>
  </section>

  <section class="card card--back" aria-label="Cara trasera">
    <div class="back__brand">
      <div class="brand-mark">WM</div>
      <p class="brand-name">Travenic Extrusion</p>
      <p class="tagline">Diseño · Extrusion · Lacado · Anodizado<br>y mecanizado de precisión de aluminio</p>
    </div>
    <div class="back__divider"></div>
    <div class="contact">
      <p class="contact__name">ANDRÉS MOLINA RIVAS</p>
      <p class="contact__role">Comercial</p>
      <ul class="contact__list">
        <li><svg viewBox="0 0 16 16" aria-hidden="true"><path d="M2 5c0-2 2-3 6-3s6 1 6 3v1h-3V4.5H5V6H2z M4 7h8l2 6H2z"/></svg>954 21 08 47</li>
        <li><svg viewBox="0 0 16 16" aria-hidden="true"><path d="M4.5 1h7a1 1 0 0 1 1 1v12a1 1 0 0 1-1 1h-7a1 1 0 0 1-1-1V2a1 1 0 0 1 1-1zm.5 2v9h6V3z"/></svg>611 42 93 05</li>
        <li><svg viewBox="0 0 16 16" aria-hidden="true"><path d="M4 1h6l2 2v3h1a1 1 0 0 1 1 1v7H2V7a1 1 0 0 1 1-1h1zm1 1v4h6V3.5L9.5 2zM5 9v1h2V9zm4 0v1h2V9zM5 11v1h2v-1zm4 0v1h2v-1z"/></svg>954 21 08 52</li>
        <li><svg viewBox="0 0 16 16" aria-hidden="true"><path d="M1 3h14v10H1zm1.5 1.2V5l5.5 4 5.5-4v-.8z"/></svg>amolina@travenic.com</li>
        <li><svg viewBox="0 0 16 16" aria-hidden="true"><circle cx="8" cy="8" r="7"/></svg>www.travenic.com</li>
      </ul>
      <address class="contact__address">
        Pol. Ind. Los Olivos, C/4 nº 22<br>
        41020 Villanueva del Río – Sevilla<br>
        Apartado de correos 305
      </address>
    </div>
  </section>

</main>
</body>
</html>
```